Epoxy coatings company needs a logo/business card design.

My company name is "Lustrous Resin Works", and I am looking for a company logo and business card design.
My initial thought was to use "Æ"in 'Lu'strous, and would also like to see ideas on how to play around with the fact that the first 3 letters (Lrw) are also the acronym of the company name.
I specialize in garage floor and interior epoxy coatings, paint flake broadcasts, quartz broadcasts, and solid color epoxy floors, concrete repairs.
I like images I've seen of a silhouetted person running a floor grinder. It keeps the design of the card simple. I'm not necessarily opposed to using images of the floors on the card, but I'd prefer to keep the front simple (Company name, my name, phone number, email) and maybe put pictures on the back. I've included a few of my personal pictures of floors I've done (including a before, after, and when the garage was being used after)
My colors are darker green (Fern/Forest/Hunter, etc), and Bronze.

Contact Information for Business Card

Name: Dana Kellworth Email: lustrousresinworks@mailbrook.net Phone: (555)318-9042 Instagram: lustrous_resin_works

Colors

Designer to choose colors to be used in the design.

Requirements
Nice to have
• I've included a business card designed for someone else, that contains the silhouette that I'm looking for. The floor grinder that I use is large like the one pictured (Torvex G40R).

```html
<!DOCTYPE html>
<html lang="en">
<head>
<meta charset="utf-8">
<title>Lustrous Resin Works – Business Card</title>
<link href="https://fonts.googleapis.com/css2?family=Poppins:wght@300;400;600;700&display=swap" rel="stylesheet">
<style>
  :root {
    --backdrop: #d9d9d9;
    --black: #141414;
    --ink: #1b1b1b;
    --green: #44574a;
    --bronze: #a8843a;
    --white: #ffffff;
    --stone-dark: #3a3a38;
    --stone-light: #9a9892;
  }
  * { box-sizing: border-box; margin: 0; padding: 0; }
  html, body {
    width: 1200px; height: 852px; overflow: hidden;
    background: var(--backdrop);
    font-family: "Poppins", sans-serif;
  }
  .canvas { position: relative; width: 1200px; height: 852px; }
  .card {
    position: absolute; width: 620px; height: 354px;
    border-radius: 22px; overflow: hidden;
    box-shadow: 0 10px 24px rgba(0,0,0,.28);
  }
  /* Service side */
  .card--services { left: 60px; top: 60px; background: var(--black); }
  .floor-photo {
    position: absolute; right: 0; top: 0; width: 66%; height: 100%;
    background:
      linear-gradient(90deg, var(--black) 0%, rgba(20,20,20,.85) 22%, rgba(20,20,20,0) 60%),
      linear-gradient(160deg, var(--stone-light) 0%, #7d7b76 35%, var(--stone-dark) 100%);
  }
  .brand {
    position: absolute; display: flex; align-items: center; gap: 10px;
    font-weight: 700; text-transform: uppercase; color: var(--bronze);
    letter-spacing: .5px; white-space: nowrap;
  }
  .brand__dot { width: 14px; height: 14px; border-radius: 50%; background: var(--bronze); }
  .card--services .brand { left: 44px; top: 126px; font-size: 24px; }
  .services {
    position: absolute; left: 44px; top: 214px; list-style: none;
    color: var(--white); font-size: 14px; line-height: 25px; text-transform: uppercase;
  }
  .services li { display: flex; align-items: center; gap: 14px; }
  .services li::before {
    content: ""; width: 7px; height: 7px; border-radius: 50%; background: var(--bronze);
  }
  /* Contact side */
  .card--contact {
    left: 520px; top: 438px;
    background: linear-gradient(200deg, var(--green) 0%, var(--green) 45%, var(--bronze) 100%);
  }
  .card--contact svg.swoosh { position: absolute; inset: 0; }
  .card--contact .brand { left: 150px; top: 276px; font-size: 22px; }
  .contact {
    position: absolute; right: 30px; top: 26px; text-align: right; color: var(--white);
  }
  .contact__name { font-size: 21px; font-weight: 300; text-transform: uppercase; line-height: 1.1; }
  .contact__name strong { font-weight: 700; }
  .contact__role { color: var(--bronze); font-weight: 700; font-size: 14px; text-transform: uppercase; margin-bottom: 12px; }
  .contact__line {
    display: flex; justify-content: flex-end; align-items: center; gap: 8px;
    font-size: 14px; font-weight: 300; line-height: 24px;
  }
  .contact__line svg { width: 13px; height: 13px; flex: none; }
</style>
</head>
<body>
<main class="canvas">
  <section class="card card--services">
    <div class="floor-photo" role="img" aria-label="Close-up photo of a glossy flake epoxy floor"></div>
    <div class="brand"><span class="brand__dot"></span>Lustrous Resin Works</div>
    <ul class="services">
      <li>Garage floor and interior epoxy coatings</li>
      <li>Paint flake broadcasts</li>
      <li>Quartz broadcasts</li>
      <li>Solid color epoxy floors</li>
    </ul>
  </section>

  <section class="card card--contact">
    <svg class="swoosh" viewBox="0 0 620 354" preserveAspectRatio="none" aria-hidden="true">
      <path d="M0,232 C150,150 420,150 620,292 L620,354 L0,354 Z" fill="var(--white)"/>
      <path d="M0,252 C160,168 420,168 620,300 L620,354 L0,354 Z" fill="var(--bronze)"/>
      <path d="M0,270 C170,186 420,186 620,312 L620,354 L0,354 Z" fill="var(--ink)"/>
    </svg>
    <div class="brand">Lustrous Resin Works</div>
    <div class="contact">
      <p class="contact__name"><strong>Dana</strong> Kellworth</p>
      <p class="contact__role">Owner</p>
      <p class="contact__line">555-318-9042
        <svg viewBox="0 0 24 24"><path fill="var(--bronze)" d="M6.6 10.8a15.1 15.1 0 0 0 6.6 6.6l2.2-2.2c.3-.3.7-.4 1-.2 1.1.4 2.3.6 3.6.6.6 0 1 .4 1 1V20c0 .6-.4 1-1 1A17 17 0 0 1 3 4c0-.6.4-1 1-1h3.5c.6 0 1 .4 1 1 0 1.3.2 2.5.6 3.6.1.3 0 .7-.2 1z"/></svg>
      </p>
      <p class="contact__line">dana@mailbrook.net
        <svg viewBox="0 0 24 24"><rect x="2" y="5" width="20" height="14" rx="2" fill="var(--bronze)"/><path d="M3 6l9 7 9-7" stroke="var(--ink)" stroke-width="1.6" fill="none"/></svg>
      </p>
      <p class="contact__line">lustrous_resin_works
        <svg viewBox="0 0 24 24"><rect x="3" y="3" width="18" height="18" rx="4" fill="none" stroke="var(--bronze)" stroke-width="2"/></svg>
      </p>
    </div>
  </section>
</main>
</body>
</html>
```